Savor and Thrive Wellbeing is being Launched and needs a business card and stationery package

I need a stationery package including business card (primary focus) , letterhead, digital letterhead, envelopes, with compliments slip, A 5 note sheet for the rebranding of my business and launch of my new website. I have a logo, like beige, brown earthy tones with a hint of red. I would also like the option of my letterhead also being printed on recycled paper in another format as well as the traditional letterhead. I do also send my letters to GPs and specialists digitally as well. I like to stand out from the usual stereotype of fruits and vegetables on business cards as I find that quite tacky and stereotypical. I want the business card to capture the essence of my logo as natural, nutrition, enjoyment, nurturing and freedom with food. I have attached the logo, and additional brief sheet on my ideas. Happy to have any background that is complementary to my theme, and what you believe would be catching. Definitely DONT'T like pink, try to pick up the darker colour in the logo please. and think too much black is a little overpowering.

Target Market(s)

clients who are interested in improving their health and wellness. Client 80% females; 20% males

Industry/Entity Type

Health And Wellness

Contact Information for Business Card

I am open to having different backgrounds as well that would complement the logo. Probably less emphasis on the heart out of the logo - just happy to keep that in the logo only please
I am also wanting two business cards - one for the appointments, one for general distribution and media distribution (both need to look consistent though) - but does give opportunity for one of the business cards to be less wordy and more striking. And the front of the business card can certainly stand out with the entire savor and thrive logo and my name and grab the attention of the receiver.
1st business card
on front:
Imogen Whitcombe
Savor and Thrive Wellbeing & logo
Nutritionist and Dietitian
Tolva Medical Centre
364 Wexley Park Rd, Halloway Q 4998
Phone: (07) 3521 7094 Fax: (07) 3617 2289
Mobile: 0400 915 268
www.savorandthrivewellbeing.example
imogen@savorandthrivewellbeing.example
on back:
next appointment

……………………….. at ……………………… (possibly 4 times)
If you are unable to keep your appointment, please contact us as soon as possible (small font)
2nd business card (needs to be very eye catching and stand out)
on front: Savor and Thrive Wellbeing logo and my name
on back:
Imogen Whitcombe
address
phones, fax, website, email address

Font styles to use
Other font styles liked:
• please refer to logo

Requirements
Must have
• refreshing and simple; new and vibrant - I am rebranding my business after 20 years
• to get a feel of what is the theme - go to my new website (not completed as yet - but you will get a preliminary view) - don't do as google search as blocked - but can put into website header and it will be shown
• www.savorandthrivewellbeing.example - but please ignore the colouring of the 4 blocks under the slider on the home page - I am not wanting these colourings - they are getting updated.
Nice to have
• earthy tones, beige, hint of red, fonts to match logo if possible, organic, modern
• get inspiration from my logo please, open to having other backgrounds that complement
Should not have
• no food shots or stereotypical weight/ scales images
• no green, yellow or orange

```html
<!DOCTYPE html>
<html lang="en">
<head>
<meta charset="utf-8">
<title>Savor and Thrive Wellbeing – Stationery Package</title>
<link href="https://fonts.googleapis.com/css2?family=Crimson+Pro:wght@400;500&family=PT+Sans+Narrow&display=swap" rel="stylesheet">
<style>
  :root{
    --paper:#e8e3d7;
    --white:#ffffff;
    --rose:#b86e68;
    --brick:#a3372a;
    --ink:#2a2420;
    --brand:#8e2f35;
    --line:#3a3330;
  }
  *{margin:0;padding:0;box-sizing:border-box}
  html,body{width:1200px;height:1200px;overflow:hidden;background:var(--white)}
  body{position:relative;font-family:"Crimson Pro",Georgia,serif;color:var(--ink)}
  .piece{position:absolute;overflow:hidden;box-shadow:0 2px 6px rgba(0,0,0,.28)}
  .paper-recycled{background:
      radial-gradient(circle at 20% 30%,rgba(255,255,255,.35),transparent 40%),
      radial-gradient(circle at 80% 70%,rgba(200,190,170,.25),transparent 45%),
      var(--paper)}
  .paper-white{background:var(--white)}
  .abs{position:absolute}
  .brand-name{font-family:"Crimson Pro",Georgia,serif;font-weight:500;color:var(--brand);line-height:1;white-space:nowrap}
  .brand-dot{display:inline-block;border-radius:50%;background:var(--brand);vertical-align:middle}
  .watermark{position:absolute;border-radius:50%;
    background:radial-gradient(circle,rgba(184,110,104,.22) 0%,rgba(184,110,104,.10) 45%,transparent 70%)}
  .watermark.on-white{background:radial-gradient(circle,rgba(184,110,104,.12) 0%,rgba(184,110,104,.05) 45%,transparent 70%)}

  /* business card */
  .card-front{left:37px;top:16px;width:482px;height:287px}
  .card-front .brand-block{left:0;width:100%;top:92px;text-align:center}
  .card-front .brand-name{font-size:29px}
  .card-front .brand-dot{width:10px;height:10px;margin-right:7px}
  .card-front .holder{left:0;width:100%;top:152px;text-align:center;font-family:"PT Sans Narrow",sans-serif;font-size:19px;line-height:23px;color:var(--ink)}
  .card-front .phones{left:349px;top:200px;font-family:"PT Sans Narrow",sans-serif;font-size:15px;line-height:24px;color:var(--ink)}
  .card-front .address{left:23px;top:246px;font-size:8px;line-height:10px}
  .card-front .web{left:164px;top:243px;font-size:9.5px;line-height:11px}

  /* appointment card */
  .card-back{left:37px;top:338px;width:482px;height:287px}
  .card-back h2{position:absolute;left:30px;top:26px;font-weight:400;font-size:18px}
  .appt-row{position:absolute;left:29px;width:270px;height:16px;font-size:11px}
  .appt-row .blank{position:absolute;bottom:0;border-bottom:1px solid var(--line)}
  .appt-row .blank.date{left:0;width:117px}
  .appt-row .blank.time{left:141px;width:129px}
  .appt-row .at{position:absolute;left:124px;bottom:1px}
  .card-back .note{left:29px;top:225px;width:260px;font-size:8.5px;line-height:11px}

  /* letterheads */
  .letter-white{left:560px;top:30px;width:483px;height:606px}
  .letter-recycled{left:784px;top:425px;width:380px;height:519px}
  .letter-head-left{font-size:8.5px;line-height:11.5px}
  .letter-head-right{text-align:right;font-size:8.5px;line-height:10px}
  .letter-head-right p+p{margin-top:9px}

  /* notes */
  .note-white{left:37px;top:659px;width:346px;height:445px}
  .note-recycled{left:406px;top:659px;width:349px;height:446px}
  .note-title{left:0;width:100%;text-align:center;font-size:9px}
  .note-foot{left:0;width:100%;text-align:center;font-size:7px;line-height:11.6px}
</style>
</head>
<body>

<section class="piece paper-recycled card-front" aria-label="Business card front">
  <svg class="abs" width="482" height="287" viewBox="0 0 482 287" style="left:0;top:0">
    <defs>
      <linearGradient id="cardCorner" x1="0" y1="0" x2="1" y2="0">
        <stop offset="0" stop-color="#e8e3d7"/>
        <stop offset="1" stop-color="#c48680"/>
      </linearGradient>
      <linearGradient id="cardBand" x1="0" y1="0" x2="1" y2="0">
        <stop offset="0" stop-color="#e8e3d7"/>
        <stop offset=".25" stop-color="#c98a84"/>
        <stop offset="1" stop-color="#b86e68"/>
      </linearGradient>
    </defs>
    <path d="M0,0 L175,0 C110,6 45,20 0,40 Z" fill="url(#cardCorner)"/>
    <path d="M0,287 L0,255 C170,240 360,190 482,52 L482,287 Z" fill="url(#cardBand)"/>
  </svg>
  <div class="abs brand-block"><span class="brand-dot"></span><span class="brand-name">Savor and Thrive Wellbeing</span></div>
  <div class="abs holder">Imogen Whitcombe<br>Nutritionist and Dietitian</div>
  <div class="abs phones">Phone: (07) 3521 7094<br>Mobile: 0400 915 268<br>Fax: (07) 3617 2289</div>
  <div class="abs address">Tolva Medical Centre<br>364 Wexley Park Rd, Halloway Q 4998</div>
  <div class="abs web">www.savorandthrivewellbeing.example<br>imogen@savorandthrivewellbeing.example</div>
</section>

<section class="piece paper-recycled card-back" aria-label="Appointment card">
  <div class="watermark" role="img" aria-label="Faint brand watermark" style="left:300px;top:20px;width:300px;height:300px"></div>
  <h2>Next appointment:</h2>
  <div class="appt-row" style="top:80px"><span class="blank date"></span><span class="at">at</span><span class="blank time"></span></div>
  <div class="appt-row" style="top:114px"><span class="blank date"></span><span class="at">at</span><span class="blank time"></span></div>
  <div class="appt-row" style="top:148px"><span class="blank date"></span><span class="at">at</span><span class="blank time"></span></div>
  <div class="appt-row" style="top:182px"><span class="blank date"></span><span class="at">at</span><span class="blank time"></span></div>
  <p class="abs note">If you are unable to keep your appointment, please contact us as soon as possible</p>
</section>

<section class="piece paper-white letter-white" aria-label="Letterhead">
  <div class="watermark on-white" role="img" aria-label="Faint brand watermark" style="left:77px;top:200px;width:300px;height:300px"></div>
  <div class="abs" style="left:29px;top:70px"><span class="brand-dot" style="width:7px;height:7px;margin-right:5px"></span><span class="brand-name" style="font-size:17px">Savor and Thrive Wellbeing</span></div>
  <div class="abs letter-head-left" style="left:29px;top:107px">Imogen Whitcombe<br>Savor and Thrive Wellbeing<br>Nutritionist and Dietitian</div>
  <div class="abs letter-head-right" style="right:32px;top:34px">
    <p>Tolva Medical Centre<br>364 Wexley Park Rd, Halloway Q 4998</p>
    <p>Phone: (07) 3521 7094<br>Fax: (07) 3617 2289<br>Mobile: 0400 915 268</p>
    <p>www.savorandthrivewellbeing.example<br>imogen@savorandthrivewellbeing.example</p>
  </div>
  <div class="abs" style="left:0;bottom:0;width:100%;height:23px;background:linear-gradient(90deg,#f5ecea 0%,#d29c96 45%,#b86e68 100%)"></div>
</section>

<section class="piece paper-recycled letter-recycled" aria-label="Recycled paper letterhead">
  <div class="watermark" role="img" aria-label="Faint brand watermark" style="left:60px;top:180px;width:270px;height:270px"></div>
  <div class="abs" style="left:12px;top:52px"><span class="brand-dot" style="width:6px;height:6px;margin-right:4px"></span><span class="brand-name" style="font-size:14px">Savor and Thrive Wellbeing</span></div>
  <div class="abs letter-head-left" style="left:12px;top:89px;font-size:7.5px;line-height:9.6px">Imogen Whitcombe<br>Savor and Thrive Wellbeing<br>Nutritionist and Dietitian</div>
  <div class="abs letter-head-right" style="right:19px;top:30px;font-size:7.5px;line-height:8.8px">
    <p>Tolva Medical Centre<br>364 Wexley Park Rd, Halloway Q 4998</p>
    <p>Phone: (07) 3521 7094<br>Fax: (07) 3617 2289<br>Mobile: 0400 915 268</p>
    <p>www.savorandthrivewellbeing.example<br>imogen@savorandthrivewellbeing.example</p>
  </div>
  <svg class="abs" width="380" height="519" viewBox="0 0 380 519" style="left:0;top:0">
    <defs>
      <linearGradient id="letterBand" x1="0" y1="0" x2="1" y2="0">
        <stop offset="0" stop-color="#f2e6e2"/>
        <stop offset=".5" stop-color="#c7877f"/>
        <stop offset="1" stop-color="#a3372a"/>
      </linearGradient>
    </defs>
    <path d="M0,519 L0,502 C150,500 320,470 380,414 L380,519 Z" fill="url(#letterBand)"/>
  </svg>
</section>

<section class="piece paper-white note-white" aria-label="Note sheet">
  <div class="watermark on-white" role="img" aria-label="Faint brand watermark" style="left:63px;top:150px;width:220px;height:220px"></div>
  <div class="abs" style="left:27px;top:40px"><span class="brand-dot" style="width:5px;height:5px;margin-right:3px"></span><span class="brand-name" style="font-size:10px">Savor and Thrive Wellbeing</span></div>
  <p class="abs note-title" style="top:66px">From the desk of your nutritionist</p>
  <div class="abs note-foot" style="top:376px">Imogen Whitcombe<br>Savor and Thrive Wellbeing<br>Mobile: 0400 915 268<br>www.savorandthrivewellbeing.example<br>imogen@savorandthrivewellbeing.example</div>
</section>

<section class="piece paper-recycled note-recycled" aria-label="Recycled note sheet">
  <div class="watermark" role="img" aria-label="Faint brand watermark" style="left:64px;top:150px;width:220px;height:220px"></div>
  <div class="abs" style="left:26px;top:32px"><span class="brand-dot" style="width:5px;height:5px;margin-right:3px"></span><span class="brand-name" style="font-size:10px">Savor and Thrive Wellbeing</span></div>
  <p class="abs note-title" style="top:64px">From the desk of your nutritionist</p>
  <div class="abs note-foot" style="top:376px">Imogen Whitcombe<br>Savor and Thrive Wellbeing<br>Mobile: 0400 915 268<br>www.savorandthrivewellbeing.example<br>imogen@savorandthrivewellbeing.example</div>
</section>

</body>
</html>
```